Newspaper Ad

Please create an ad for a newspaper that is 10.5 wide and 13 inches long. Please highlight the features of the property and ensure that the name of our firm (Birchwood Hollow Realty) is the same size as our phone number which is 717-530-6198.

Pemberton's Crossing and The residences at 9 N. Ash
9 N. Ash Street, Quarryville PA

Now leasing 1, 2 & 3 bedroom units available this spring. Newley renovated apartments with stainless appliances, hardwood floors, granite countertops, in unit laundry. Includes water, sewer trash and off street parking. 1200sq first floor retail available.

717.530.6198 or www.BirchwoodHollowRealty.example for details.

```html
<!DOCTYPE html>
<html lang="en">
<head>
<meta charset="utf-8">
<title>Pemberton's Crossing – Newspaper Ad</title>
<link href="https://fonts.googleapis.com/css2?family=Fjalla+One&family=Montserrat:wght@500;600;700&display=swap" rel="stylesheet">
<style>
  :root {
    --page-bg: #e9e4dc;
    --sheet: #ffffff;
    --thumb-band: #ececec;
    --teal: #1f6569;
    --teal-dark: #17565a;
    --charcoal: #333638;
    --silver-light: #f2f2f2;
    --silver-dark: #a9acae;
    --ink: #2a2a2a;
    --sky: #a9bfd6;
    --facade: #7e847f;
    --road: #3b3b3d;
  }
  * { box-sizing: border-box; margin: 0; padding: 0; }
  html, body { width: 1200px; height: 2168px; overflow: hidden; }
  body { background: var(--page-bg); position: relative; font-family: "Montserrat", sans-serif; }

  .ad {
    position: absolute; left: 40px; top: 390px;
    width: 1021px; height: 1264px;
    transform: scale(1.097); transform-origin: 0 0;
    background: var(--sheet);
    box-shadow: 0 10px 30px rgba(0,0,0,.25);
    overflow: hidden;
  }

  .hero {
    position: absolute; left: 0; top: 0; width: 1021px; height: 545px;
    background: linear-gradient(180deg, var(--sky) 0%, #d6e0ea 45%, var(--facade) 62%, #6f7470 80%, var(--road) 100%);
  }

  .gallery {
    position: absolute; left: 0; top: 545px; width: 1021px; height: 244px;
    background: var(--thumb-band);
  }
  .thumb {
    position: absolute; top: 32px; width: 280px; height: 177px;
    border: 6px solid #fff;
    box-shadow: 0 12px 10px -6px rgba(0,0,0,.45);
    background: linear-gradient(180deg, var(--sky) 0%, #d3dde7 40%, var(--facade) 60%, #777c78 82%, var(--road) 100%);
  }
  .thumb--one { left: 56px; }
  .thumb--two { left: 371px; }
  .thumb--three { left: 686px; }

  .details {
    position: absolute; left: 0; top: 789px; width: 1021px; height: 281px;
    background: var(--teal);
  }
  .title-banner {
    position: absolute; left: 193px; top: 28px; width: 635px; height: 49px;
    background: linear-gradient(180deg, var(--silver-light), var(--silver-dark));
    clip-path: polygon(3% 0, 100% 0, 97% 100%, 0 100%);
    font-family: "Fjalla One", sans-serif; font-size: 27px; color: var(--teal);
    display: flex; align-items: center; justify-content: center; letter-spacing: .2px;
  }
  .address-banner {
    position: absolute; left: 293px; top: 77px; width: 435px; height: 44px;
    background: var(--charcoal);
    clip-path: polygon(0 0, 100% 0, 95% 100%, 5% 100%);
    color: #fff; font-weight: 700; font-size: 19px;
    display: flex; align-items: center; justify-content: center;
  }
  .features {
    position: absolute; top: 156px; list-style: none;
    color: #fff; font-weight: 600; font-size: 15px; line-height: 21px;
  }
  .features--left { left: 56px; width: 470px; }
  .features--right { left: 549px; width: 440px; }
  .features li { position: relative; padding-left: 22px; margin-bottom: 17px; }
  .features li svg { position: absolute; left: 0; top: 3px; width: 15px; height: 15px; }

  .contact {
    position: absolute; left: 0; top: 1070px; width: 1021px; height: 194px;
    background: var(--sheet);
  }
  .firm-name {
    position: absolute; left: 65px; top: 42px; width: 430px;
    display: flex; align-items: center; gap: 16px;
    font-weight: 700; font-size: 40px; line-height: 44px; color: var(--ink);
  }
  .firm-name .mark { width: 22px; height: 22px; background: var(--teal); flex: none; }
  .phone {
    position: absolute; left: 589px; top: 66px; width: 324px; height: 50px;
    border: 2px solid var(--charcoal); border-radius: 25px;
    display: flex; align-items: center; justify-content: center; gap: 8px;
    font-weight: 700; font-size: 40px; color: var(--teal); letter-spacing: -.5px;
  }
  .phone svg { width: 34px; height: 34px; }
  .website {
    position: absolute; left: 536px; top: 130px; width: 420px;
    display: flex; align-items: center; gap: 6px;
    font-size: 20px; font-weight: 500; color: var(--charcoal);
  }
  .website strong { color: var(--teal); font-weight: 700; }
  .website svg { width: 18px; height: 18px; }
</style>
</head>
<body>
  <article class="ad">
    <div class="hero" role="img" aria-label="Rendering of the renovated two-storey corner building with porches and storefront under a cloudy sky"></div>

    <section class="gallery">
      <div class="thumb thumb--one" role="img" aria-label="Corner view rendering of the building"></div>
      <div class="thumb thumb--two" role="img" aria-label="Side street view rendering of the building"></div>
      <div class="thumb thumb--three" role="img" aria-label="Rendering of the front porch entrance"></div>
    </section>

    <section class="details">
      <h1 class="title-banner">Pemberton's Crossing and The residences at 9 N. Ash</h1>
      <h2 class="address-banner">9 N. Ash Street, Quarryville PA</h2>
      <ul class="features features--left">
        <li><svg viewBox="0 0 16 16"><circle cx="8" cy="8" r="6.5" fill="none" stroke="#fff" stroke-width="1.3"/><path d="M5 8.2l2 2 4-4" fill="none" stroke="#fff" stroke-width="1.3"/></svg>Now leasing 1, 2 &amp; 3 bedroom units available this spring.</li>
        <li><svg viewBox="0 0 16 16"><circle cx="8" cy="8" r="6.5" fill="none" stroke="#fff" stroke-width="1.3"/><path d="M5 8.2l2 2 4-4" fill="none" stroke="#fff" stroke-width="1.3"/></svg>Newley renovated apartments with stainless appliances, hardwood floors, granite countertops, in unit laundry.</li>
      </ul>
      <ul class="features features--right">
        <li><svg viewBox="0 0 16 16"><circle cx="8" cy="8" r="6.5" fill="none" stroke="#fff" stroke-width="1.3"/><path d="M5 8.2l2 2 4-4" fill="none" stroke="#fff" stroke-width="1.3"/></svg>Includes water, sewer trash and off street parking.</li>
        <li><svg viewBox="0 0 16 16"><circle cx="8" cy="8" r="6.5" fill="none" stroke="#fff" stroke-width="1.3"/><path d="M5 8.2l2 2 4-4" fill="none" stroke="#fff" stroke-width="1.3"/></svg>1200sq first floor retail available.</li>
      </ul>
    </section>

    <footer class="contact">
      <div class="firm-name"><span class="mark"></span><span>Birchwood Hollow Realty</span></div>
      <div class="phone">
        <svg viewBox="0 0 34 34"><circle cx="17" cy="17" r="16" fill="#1f6569"/><path d="M11.5 9.5c1-.8 2-.6 2.6.4l1.5 2.6c.5.9.3 1.7-.5 2.3l-1 .7c.9 2 2.4 3.6 4.4 4.6l.8-1c.6-.8 1.5-1 2.3-.5l2.6 1.5c1 .6 1.1 1.7.3 2.6-1.6 1.9-3.4 2.2-5.5 1.2-4-1.9-7-5-8.6-9-.8-2 -.4-3.8 1.1-5.4z" fill="#fff"/></svg>
        <span>717.530.6198</span>
      </div>
      <div class="website">
        <svg viewBox="0 0 18 18"><circle cx="9" cy="9" r="7.5" fill="none" stroke="#1f6569" stroke-width="1.5"/><ellipse cx="9" cy="9" rx="3.3" ry="7.5" fill="none" stroke="#1f6569" stroke-width="1.3"/><path d="M1.5 9h15M3 5h12M3 13h12" stroke="#1f6569" stroke-width="1.2"/></svg>
        <span>www.<strong>BirchwoodHollowRealty</strong>.example</span>
      </div>
    </footer>
  </article>
</body>
</html>
```